business card for a shoe shop

we would like a business card for a family owned shoe shop.
With this information included.
Dunleavy's Shoe Store
Family owned since 1947

then on other side
Dunleavy's Shoe Store
Footwear fitting specialist
Phone: 9471 2386
218 Tarn St, Wexley Heights 3091
(cnr. Corrigan Rd and Tarn St)
dunleavyshoes218@quillmail.example
if could incorporate the purple color on card i have attached.

```html
<!DOCTYPE html>
<html lang="en">
<head>
<meta charset="utf-8">
<title>Dunleavy's Shoe Store — Business Card</title>
<link rel="stylesheet" href="https://fonts.googleapis.com/css2?family=Roboto+Condensed:wght@700&family=Roboto:wght@400;500;700&display=swap">
<style>
  :root {
    --stage: #b9b9b5;
    --paper: #ffffff;
    --brand-purple: #8e479d;
    --brand-purple-deep: #7f3d8f;
    --brand-purple-light: #9a57a8;
    --ink-purple: #8a3d9b;
    --reverse: #ffffff;
  }
  * { box-sizing: border-box; margin: 0; padding: 0; }
  html, body {
    width: 1200px;
    height: 810px;
    overflow: hidden;
    background: var(--stage);
  }
  .sheet {
    width: 1200px;
    height: 810px;
    display: flex;
    flex-direction: column;
    align-items: center;
    justify-content: center;
    gap: 40px;
  }
  .card {
    width: 620px;
    height: 354px;
    position: relative;
    overflow: hidden;
    box-shadow: 0 10px 24px rgba(0, 0, 0, 0.22);
  }

  /* Front: contact side */
  .card--front {
    background: var(--paper);
    border-bottom: 4px solid var(--brand-purple);
    color: var(--ink-purple);
    display: flex;
    flex-direction: column;
    align-items: center;
    justify-content: center;
    text-align: center;
    font-family: "Roboto", sans-serif;
  }
  .front__name {
    font-family: "Roboto Condensed", sans-serif;
    font-weight: 700;
    font-size: 36px;
    letter-spacing: 0.5px;
    line-height: 1;
    text-transform: uppercase;
  }
  .front__tagline {
    font-size: 21px;
    margin-top: 4px;
  }
  .front__details {
    margin-top: 34px;
    font-size: 20px;
    line-height: 1.32;
  }
  .front__details strong { font-weight: 700; }

  /* Back: brand side */
  .card--back {
    background: var(--brand-purple);
  }
  .back__texture {
    position: absolute;
    inset: 0;
    background:
      radial-gradient(circle at 30% 40%, var(--brand-purple-light) 0%, transparent 55%),
      linear-gradient(135deg, var(--brand-purple) 0%, var(--brand-purple-deep) 100%);
  }
  .back__brand {
    position: absolute;
    left: 50%;
    top: 50%;
    transform: translate(-50%, -50%);
    display: flex;
    align-items: center;
    gap: 18px;
    color: var(--reverse);
    font-family: "Roboto", sans-serif;
  }
  .back__mark {
    flex: none;
    width: 62px;
    height: 62px;
    background: var(--reverse);
  }
  .back__text {
    display: flex;
    flex-direction: column;
    align-items: center;
    white-space: nowrap;
  }
  .back__name {
    font-weight: 500;
    font-size: 22px;
    line-height: 1.15;
    letter-spacing: 1px;
    text-transform: uppercase;
    text-align: center;
  }
  .back__name-row {
    display: flex;
    align-items: center;
    gap: 8px;
  }
  .back__rule {
    width: 54px;
    height: 1.5px;
    background: var(--reverse);
  }
  .back__since {
    margin-top: 10px;
    font-weight: 400;
    font-size: 15px;
    letter-spacing: 1px;
  }
</style>
</head>
<body>
  <main class="sheet">
    <section class="card card--front" aria-label="Business card front">
      <h1 class="front__name">Dunleavy's Shoe Store</h1>
      <p class="front__tagline">Footwear Fitting Specialist</p>
      <div class="front__details">
        <p><strong>Phone:</strong> 9471 2386</p>
        <p><strong>Email:</strong> dunleavyshoes218@quillmail.example</p>
        <p><strong>Address:</strong> 218 Tarn St, Wexley Heights 3091</p>
        <p>(cnr. Corrigan Rd and Tarn St)</p>
      </div>
    </section>

    <section class="card card--back" aria-label="Business card back">
      <div class="back__texture" role="img" aria-label="Tonal embossed brand pattern in purple"></div>
      <div class="back__brand">
        <span class="back__mark" aria-hidden="true"></span>
        <div class="back__text">
          <p class="back__name">Dunleavy's Shoe</p>
          <div class="back__name-row">
            <span class="back__rule" aria-hidden="true"></span>
            <p class="back__name">Store</p>
            <span class="back__rule" aria-hidden="true"></span>
          </div>
          <p class="back__since">Family owned since 1947</p>
        </div>
      </div>
    </section>
  </main>
</body>
</html>
```